Vent doux

Hello,
I’m a designer sunglasses reatail Store owner in Montreal, Quebec.

Looking for something modern, fresh with a trendy appeal.

Will send my logo.
Thank you.

Store

```html
<!DOCTYPE html>
<html lang="fr">
<head>
<meta charset="utf-8">
<title>Vent doux — cartes de visite</title>
<link href="https://fonts.googleapis.com/css2?family=Source+Sans+3:wght@400;600;700&display=swap" rel="stylesheet">
<style>
  :root {
    --red: #bc1428;
    --grey: #a6a6a6;
    --ink: #222222;
    --white: #ffffff;
    --page: #ffffff;
  }
  * { margin: 0; padding: 0; box-sizing: border-box; }
  html, body { width: 1200px; height: 1200px; overflow: hidden; background: var(--page); }
  body { position: relative; font-family: "Source Sans 3", sans-serif; }

  .card {
    position: absolute;
    left: 131px;
    width: 900px;
    height: 540px;
    overflow: hidden;
    box-shadow: 10px 12px 18px rgba(0,0,0,0.35);
  }
  .card--front { top: 26px; background: var(--red); }
  .card--back { top: 599px; background: var(--grey); }

  .side-tab { position: absolute; top: 238px; width: 61px; height: 243px; }
  .side-tab--left { left: 0; }
  .side-tab--right { right: 0; }
  .card--front .side-tab polygon { fill: var(--grey); }
  .card--back .side-tab polygon { fill: var(--red); }

  .brand {
    position: absolute;
    display: flex;
    align-items: center;
    font-weight: 600;
    text-transform: uppercase;
    line-height: 1;
  }
  .brand__dot { border-radius: 50%; flex: none; }
  .card--front .brand {
    left: 0; right: 0; top: 222px;
    justify-content: center;
    gap: 26px;
    font-size: 82px;
    letter-spacing: 6px;
    color: var(--white);
  }
  .card--front .brand__dot { width: 60px; height: 60px; background: var(--white); }
  .card--back .brand {
    left: 65px; top: 120px;
    gap: 30px;
    font-size: 104px;
    letter-spacing: 8px;
    color: var(--ink);
  }
  .card--back .brand__dot { width: 76px; height: 76px; background: var(--red); }

  .front-site {
    position: absolute;
    left: 0; right: 0; top: 448px;
    text-align: center;
    color: var(--white);
    font-size: 17px;
    font-weight: 600;
  }

  .holder-name {
    position: absolute;
    left: 150px; top: 350px;
    width: 265px;
    text-align: right;
    font-size: 31px;
    font-weight: 700;
    color: var(--ink);
  }
  .divider {
    position: absolute;
    left: 434px; top: 290px;
    width: 2px; height: 152px;
    background: var(--red);
  }
  .contact { position: absolute; left: 448px; top: 286px; list-style: none; color: var(--ink); font-size: 18px; line-height: 23px; }
  .contact__item { display: flex; align-items: flex-start; gap: 14px; margin-bottom: 10px; }
  .contact__item:nth-child(2) { margin-bottom: 14px; }
  .contact__item:nth-child(3) { margin-bottom: 16px; }
  .contact__icon { width: 26px; height: 22px; flex: none; margin-top: 1px; }
  .contact__icon * { fill: var(--red); }
</style>
</head>
<body>

<section class="card card--front" aria-label="Recto">
  <svg class="side-tab side-tab--left" viewBox="0 0 61 243"><polygon points="0,0 29,0 61,21 61,219 29,243 0,243"/></svg>
  <svg class="side-tab side-tab--right" viewBox="0 0 61 243"><polygon points="61,0 32,0 0,21 0,219 32,243 61,243"/></svg>
  <div class="brand"><span class="brand__dot"></span><span class="brand__name">Vent doux</span></div>
  <p class="front-site">www.ventdoux.ca</p>
</section>

<section class="card card--back" aria-label="Verso">
  <svg class="side-tab side-tab--left" viewBox="0 0 61 243"><polygon points="0,0 29,0 61,21 61,219 29,243 0,243"/></svg>
  <svg class="side-tab side-tab--right" viewBox="0 0 61 243"><polygon points="61,0 32,0 0,21 0,219 32,243 61,243"/></svg>
  <div class="brand"><span class="brand__dot"></span><span class="brand__name">Vent doux</span></div>

  <p class="holder-name">LÉA MARCHAND</p>
  <span class="divider"></span>
  <ul class="contact">
    <li class="contact__item">
      <svg class="contact__icon" viewBox="0 0 26 22"><path d="M13 0a8 8 0 0 0-8 8c0 6 8 14 8 14s8-8 8-14a8 8 0 0 0-8-8zm0 11a3 3 0 1 1 0-6 3 3 0 0 1 0 6z"/></svg>
      <span>415 Rue Saint-Denis, Local 12<br>Montréal, QC H2X 3K8</span>
    </li>
    <li class="contact__item">
      <svg class="contact__icon" viewBox="0 0 26 22"><path d="M6 1l4 5-2 3c1 3 3 5 6 6l3-2 5 4-3 4C10 21 3 14 2 4z"/></svg>
      <span>514 555 0192</span>
    </li>
    <li class="contact__item">
      <svg class="contact__icon" viewBox="0 0 26 22"><path d="M1 5h24v13H1zm2 2v1l10 6 10-6V7L13 12z"/></svg>
      <span>bonjour@ventdoux.ca</span>
    </li>
    <li class="contact__item">
      <svg class="contact__icon" viewBox="0 0 26 22"><path d="M13 0a11 11 0 1 0 0 22 11 11 0 0 0 0-22zm0 2a9 9 0 0 1 6 2l-3 2-3-1-2 3 3 3v4l-2 3A9 9 0 0 1 5 6l3 3 2-2-1-4a9 9 0 0 1 4-1z"/></svg>
      <span>www.ventdoux.ca</span>
    </li>
  </ul>
</section>

</body>
</html>
```